Coffee and Plastics

I am looking for a completely new site that shows the products we have. Our current site is www.velmorebrothersroast.com. We are open minded to what designers come up with. Our current site is www.velmorebrothersroast.com. You can you the information from there to start the site. I need these tabs on the main home page. ( Home, Coffee & Tea, Condiments, and Paper and Plastics, and Contact.) You can take photos and info from my Current site. In products page.
I will be uploading info and photo for paper and plastics.
Look and feel
Each slider illustrates characteristics of the customer's brand and the style your logo design should communicate.

```html
<!DOCTYPE html>
<html lang="en">
<head>
<meta charset="utf-8">
<title>Velmore Brothers Roast</title>
<link href="https://fonts.googleapis.com/css2?family=Oswald:wght@300;400;500&family=Open+Sans:ital,wght@0,400;0,600;1,400&display=swap" rel="stylesheet">
<style>
:root{
  --burlap:#c4b48c;
  --burlap-dark:#a8976d;
  --brick:#a5311a;
  --brick-dark:#7c2110;
  --cream:#fbf4e4;
  --panel:#e3d4c6;
  --panel-top:#d49a85;
  --page:#9c8468;
  --ink:#2d2621;
  --heading:#a3361d;
  --footer:#545454;
  --footer-deep:#2e2e2e;
  --footer-text:#e6e6e6;
  --footer-muted:#b9b9b9;
}
*{box-sizing:border-box;margin:0;padding:0}
html,body{width:858px;height:1200px;overflow:hidden}
body{font-family:"Open Sans",sans-serif;color:var(--ink);background:var(--page)}
h1,h2,h3,h4{font-weight:400}
.canvas{position:relative;width:858px;height:1200px;overflow:hidden;background:linear-gradient(90deg,#8f7659,#b29a7c 30%,#b29a7c 70%,#8f7659)}
.abs{position:absolute}

/* header */
.site-header{left:0;top:0;width:858px;height:97px;background:radial-gradient(ellipse at 50% 40%,#d2c39c,var(--burlap) 60%,var(--burlap-dark));border-bottom:3px solid #efe8d8}
.brand{left:112px;top:14px;color:var(--cream);font-family:"Oswald",sans-serif;font-weight:400;text-align:center;width:320px}
.brand-name{font-size:29px;letter-spacing:1px;line-height:1.1}
.brand-phone{font-size:17px;line-height:1.25}
.brand-hours{font-size:14px;line-height:1.3}
.social{top:13px;width:22px;height:22px;border-radius:50%;background:#3c82c6;border:2px solid #e8eef4}
.mail{left:574px;top:68px;display:flex;align-items:center;gap:5px;font-family:"Oswald",sans-serif;font-weight:300;font-size:15px;color:#2b2520}

/* nav */
.main-nav{left:0;top:97px;width:858px;height:21px;background:linear-gradient(#b43a20,var(--brick));border-bottom:1px solid var(--brick-dark)}
.main-nav a{position:absolute;top:2px;color:#fff;text-decoration:none;font-family:"Oswald",sans-serif;font-size:12px;letter-spacing:.4px}

/* slider */
.hero{left:97px;top:118px;width:664px;height:240px}
.hero-photo{position:absolute;inset:0;background:linear-gradient(180deg,#5e3d26,#3f2616 60%,#4d2d18)}
.hero-title{left:15px;top:26px;color:#fff;font-family:"Oswald",sans-serif;font-weight:500;font-size:25px;line-height:28px;letter-spacing:.5px;text-transform:uppercase;text-shadow:1px 1px 3px rgba(0,0,0,.6)}
.hero-arrow{top:105px;width:30px;height:30px;border-radius:50%;background:rgba(240,230,220,.75);border:1px solid #b9a99b}
.hero-dots{left:303px;top:224px;display:flex;gap:4px}
.hero-dots span{width:11px;height:11px;background:#fff;border:1px solid #bbb}
.hero-dots span.is-active{background:#b9543e}

/* content */
.content{left:97px;top:358px;width:664px;height:684px;background:linear-gradient(180deg,var(--panel-top) 0,#d8bcae 30px,var(--panel) 70px,var(--panel))}
.welcome-title{left:13px;top:20px;font-family:"Oswald",sans-serif;font-weight:300;font-size:28px;line-height:1.3;color:var(--heading)}
.welcome-copy{left:14px;top:66px;width:340px;font-size:9.3px;line-height:13.7px;color:#2f2a26}
.welcome-copy p{margin-bottom:13.7px}
.welcome-photo{left:362px;top:66px;width:302px;height:180px;background:linear-gradient(135deg,#d9cdc0,#9c7a5c 60%,#6e4c33)}

.card{top:293px;width:190px;height:207px;background:#fff;border-top:3px solid var(--brick);box-shadow:0 1px 4px rgba(0,0,0,.25)}
.card-title{position:absolute;top:9px;left:0;width:100%;display:flex;align-items:center;justify-content:center;gap:5px;font-family:"Oswald",sans-serif;font-weight:400;font-size:19px;line-height:24px;color:var(--heading);white-space:nowrap}
.card-title i{flex:1;height:6px;border-top:1px solid var(--brick);border-bottom:1px solid var(--brick);margin:0 6px}
.card-photo{position:absolute;left:8px;top:38px;width:174px;height:99px;background:linear-gradient(135deg,#d9cba5,#b59d6b)}
.card-text{position:absolute;left:8px;top:145px;width:174px;font-size:9.3px;line-height:11.3px;text-align:center;color:#2f2a26}
.card-btn{position:absolute;left:44px;top:194px;width:100px;height:25px;background:linear-gradient(#b23d22,#9a2c15);border-bottom:3px solid var(--brick-dark);color:#fff;font-size:8px;display:flex;align-items:center;justify-content:center;gap:4px}

.clients{left:9px;top:534px;width:645px;height:136px;border:3px solid #cf8f7e;border-radius:5px;background:linear-gradient(180deg,#8c6748,#a98a6c 50%,#7a5638)}
.clients-title{left:6px;top:20px;display:flex;align-items:center;gap:6px;color:#fff;font-family:"Oswald",sans-serif;font-weight:300;font-size:19px}
.clients-title i{display:block;width:312px;height:8px;border-top:2px solid #f3ece4;border-bottom:2px solid #f3ece4}
.clients-strip{left:35px;top:56px;width:570px;height:58px;background:#eeeeee;border:1px solid #cfcfcf;display:flex;align-items:center;gap:8px;padding:0 10px}
.badge{height:34px;background:#c7c7c7;border-radius:3px}
.clients-arrow{top:70px}

/* footer */
.site-footer{left:0;top:1042px;width:858px;height:135px;background:var(--footer)}
.footer-heading{font-size:15px;line-height:18px;font-style:italic;font-weight:400;color:var(--footer-muted)}
.footer-links{left:110px;top:12px}
.footer-links ul{list-style:none;margin-top:3px}
.footer-links li{font-size:11px;line-height:19px;color:var(--footer-text)}
.footer-rule{top:12px;width:1px;height:108px;background:#6c6c6c}
.quick{left:318px;top:12px;width:164px}
.quick .footer-heading{margin-left:3px}
.field{margin-top:5px;height:24px;border:1px solid #7a7a7a;border-radius:3px;background:#4b4b4b;font-size:9px;font-style:italic;color:#bdbdbd;padding:5px 10px}
.send{margin:7px 0 0 23px;width:116px;height:24px;background:linear-gradient(#b33c21,#9b2c15);border-bottom:3px solid var(--brick-dark);color:#fff;font-size:9px;font-style:italic;display:flex;align-items:center;justify-content:center}
.contact-info{left:597px;top:12px}
.contact-info ul{list-style:none;margin-top:3px}
.contact-info li{display:flex;align-items:center;gap:5px;font-size:11px;line-height:19px;color:var(--footer-text)}
.contact-info li svg{width:11px;flex:none}
.contact-info small{font-size:8px;font-style:italic}
.copyright{left:0;top:1177px;width:858px;height:23px;background:var(--footer-deep);color:#bdbdbd;font-size:8.5px;text-align:center;line-height:23px;letter-spacing:.3px}
</style>
</head>
<body>
<div class="canvas">

  <header class="site-header abs">
    <div class="brand abs">
      <div class="brand-name">Velmore Brothers Roast</div>
      <div class="brand-phone">1-800-555-0147</div>
      <div class="brand-hours">Mon – Fri 9 – 5 Central Time</div>
    </div>
    <span class="social abs" style="left:661px"></span>
    <span class="social abs" style="left:692px"></span>
    <span class="social abs" style="left:723px"></span>
    <div class="mail abs">
      <svg width="17" height="12" viewBox="0 0 17 12"><rect x=".5" y=".5" width="16" height="11" fill="#e0642d" stroke="#a5311a"/><path d="M.5 .5 8.5 7 16.5 .5" fill="none" stroke="#fff" stroke-width="1.2"/></svg>
      velmorebrothers@example.com
    </div>
  </header>

  <nav class="main-nav abs">
    <a style="left:116px">Home</a>
    <a style="left:179px">Coffee &amp; Tea</a>
    <a style="left:287px">Condiments</a>
    <a style="left:384px">Paper and Plastics</a>
    <a style="left:519px">Contact</a>
  </nav>

  <section class="hero abs">
    <div class="hero-photo" role="img" aria-label="Photo: coffee cup on a saucer beside a burlap sack and scoop of roasted coffee beans"></div>
    <h1 class="hero-title abs">We guarantee all of our products will<br>meet your level of satisfaction.</h1>
    <svg class="hero-arrow abs" style="left:20px" viewBox="0 0 30 30"><path d="M17 9 11 15 17 21" fill="none" stroke="#a5311a" stroke-width="2"/></svg>
    <svg class="hero-arrow abs" style="left:624px" viewBox="0 0 30 30"><path d="M13 9 19 15 13 21" fill="none" stroke="#a5311a" stroke-width="2"/></svg>
    <div class="hero-dots abs"><span class="is-active"></span><span></span><span></span><span></span></div>
  </section>

  <main class="content abs">
    <h2 class="welcome-title abs">Welcome to Velmore Brothers Roast</h2>
    <div class="welcome-copy abs">
      <p>We are a family-owned and operated business based in Marlow Texas. Since the opening of Velmore Brothers Roast plant in 1995, we have become Texas' premier independently owned coffee packaging company. Our success relies solely on the principle of selling only the freshest, highest-quality in-room coffee available.</p>
      <p>Velmore Brothers packages and supplies in-room coffee, tea products, and condiments. Whether we're supplying a 50-room Hotel or a 500-room grand resort, we have the distribution capacity to fill your rooms with the most aromatic and robust coffees and teas available at competitive prices.</p>
      <p>Velmore Brothers is continuously striving for ways to improve quality and product appearance to meet the highest standards in today's franchises and independent hotels. We are very aware that our success depends entirely upon maintaining our customers' confidence in our products, so we pay close attention to your needs every step of the way.</p>
    </div>
    <div class="welcome-photo abs" role="img" aria-label="Photo: white branded coffee mug beside a burlap sack spilling coffee beans"></div>

    <article class="card abs" style="left:19px">
      <h3 class="card-title"><i></i>Coffee &amp; Tea<i></i></h3>
      <div class="card-photo" role="img" aria-label="Photo: kettle, tea packets and canisters of ground coffee"></div>
      <p class="card-text">Lorem Ipsum. Proin gravida nibh velit auctor aliquet. Aenean sollicitudin, lorem quis bibendum auctor, nisi elit consequat ipsum..</p>
      <span class="card-btn">Learn more <svg width="9" height="6" viewBox="0 0 9 6"><path d="M0 3H7M5 .5 8 3 5 5.5" fill="none" stroke="#f0a58e" stroke-width="1.3"/></svg></span>
    </article>
    <article class="card abs" style="left:236px">
      <h3 class="card-title"><i></i>Condiments<i></i></h3>
      <div class="card-photo" role="img" aria-label="Photo: sugar, creamer and stirrer packets"></div>
      <p class="card-text">Lorem Ipsum. Proin gravida nibh velit auctor aliquet. Aenean sollicitudin, lorem quis bibendum auctor, nisi elit consequat ipsum..</p>
      <span class="card-btn">Learn more <svg width="9" height="6" viewBox="0 0 9 6"><path d="M0 3H7M5 .5 8 3 5 5.5" fill="none" stroke="#f0a58e" stroke-width="1.3"/></svg></span>
    </article>
    <article class="card abs" style="left:454px">
      <h3 class="card-title"><i></i>Paper and Plastics<i></i></h3>
      <div class="card-photo" role="img" aria-label="Photo: plastic cutlery, a cup and a divided food tray"></div>
      <p class="card-text">Lorem Ipsum. Proin gravida nibh velit auctor aliquet. Aenean sollicitudin, lorem quis bibendum auctor, nisi elit consequat ipsum..</p>
      <span class="card-btn">Learn more <svg width="9" height="6" viewBox="0 0 9 6"><path d="M0 3H7M5 .5 8 3 5 5.5" fill="none" stroke="#f0a58e" stroke-width="1.3"/></svg></span>
    </article>

    <section class="clients abs" role="img" aria-label="Coffee beans backdrop behind a strip of partner hotel badges">
      <h3 class="clients-title abs">Serving Fine Establishments Everywhere!<i></i></h3>
      <svg class="clients-arrow abs" style="left:8px" width="24" height="30" viewBox="0 0 24 30"><path d="M18 3 6 15 18 27" fill="none" stroke="#fff" stroke-width="5"/></svg>
      <div class="clients-strip abs">
        <span class="badge" style="width:92px"></span>
        <span class="badge" style="width:66px"></span>
        <span class="badge" style="width:36px;border-radius:50%"></span>
        <span class="badge" style="width:168px"></span>
        <span class="badge" style="width:52px"></span>
        <span class="badge" style="width:36px"></span>
        <span class="badge" style="width:30px"></span>
        <span class="badge" style="width:30px"></span>
      </div>
      <svg class="clients-arrow abs" style="left:611px" width="24" height="30" viewBox="0 0 24 30"><path d="M6 3 18 15 6 27" fill="none" stroke="#fff" stroke-width="5"/></svg>
    </section>
  </main>

  <footer class="site-footer abs">
    <div class="footer-links abs">
      <h4 class="footer-heading">Sitemap</h4>
      <ul><li>Home</li><li>Coffee &amp; Tea</li><li>Condiments</li><li>Paper and Plastics</li><li>Contact</li></ul>
    </div>
    <span class="footer-rule abs" style="left:258px"></span>
    <div class="quick abs">
      <h4 class="footer-heading">Quick contact</h4>
      <div class="field">Name</div>
      <div class="field">Email</div>
      <div class="send">Send</div>
    </div>
    <span class="footer-rule abs" style="left:538px"></span>
    <div class="contact-info abs">
      <h4 class="footer-heading">Contact info</h4>
      <ul>
        <li><svg viewBox="0 0 11 14" height="14"><path d="M5.5 13S1 7.5 1 5a4.5 4.5 0 0 1 9 0c0 2.5-4.5 8-4.5 8Z" fill="none" stroke="#ccc" stroke-width="1.2"/><circle cx="5.5" cy="5" r="1.6" fill="#ccc"/></svg>Velmore Brothers</li>
        <li><span style="width:11px"></span>Marlow, Texas</li>
        <li><svg viewBox="0 0 11 9" height="9"><path d="M1 3C3 0 8 0 10 3L8.5 4 7 2.5H4L2.5 4ZM3 4H8L9.5 8.5H1.5Z" fill="#ccc"/></svg>1-800-555-0147 (<small>Toll Free</small>)</li>
        <li><svg viewBox="0 0 11 10" height="10"><rect x="3" y="0.5" width="5" height="3" fill="none" stroke="#ccc"/><rect x=".5" y="3.5" width="10" height="4.5" fill="#ccc"/><rect x="3" y="6.5" width="5" height="3" fill="#545454" stroke="#ccc"/></svg>903-555-0162</li>
        <li><svg viewBox="0 0 11 9" height="9"><rect x=".5" y=".5" width="10" height="8" fill="none" stroke="#ccc"/><path d="M.5 .5 5.5 5 10.5 .5" fill="none" stroke="#ccc"/></svg>VelmoreBrothers@example.com</li>
      </ul>
    </div>
  </footer>
  <div class="copyright abs">Copyright © 2014 &nbsp;Velmore Brothers Roast &nbsp;| All Rights Reserved.</div>

</div>
</body>
</html>
```